Business card for communications

Need a business card for my consulting business - I work with not for profits, start ups and social enterprises on their media, communications campaigns.

Please see my website for colours, images and fonts www.morvenquillet.example

Morven Quillet
Communications & Campaign strategist
Sydney - Melbourne
M: 0498 317 250
E: morven@morvenquillet.example
S: morvenquillet
W: morvenquillet.example
T: @morvenquillet

(above is info only and can be presented any way e.g. should not have to be M for mobile - it should be an icon)
Updates

Dear designers I have updated the brief and uploaded high res images from my website for you to use. The designs so far with the use of images and icons are much better so far. Thank you I look forward to receiving your revised designs. Morven Quillet

Industry/Entity Type

Communications

Font styles to use
Sans Serif

Requirements
Must have
• Icons for contact details
Images from the website www.morvenquillet.example
Nice to have
• Images - attached

```html
<!DOCTYPE html>
<html lang="en">
<head>
<meta charset="utf-8">
<title>Morven Quillet – Business Card</title>
<link href="https://fonts.googleapis.com/css2?family=Lato:wght@400;700;900&display=swap" rel="stylesheet">
<style>
  :root {
    --backdrop: #e9e6e1;
    --card-white: #ffffff;
    --card-shade: #eeeeee;
    --gold: #e9b526;
    --gold-line: #efd27a;
    --yellow: #f4cd08;
    --yellow-deep: #e6b800;
    --orange: #e39f1e;
    --orange-deep: #d48a17;
    --ink: #4a4a4a;
    --photo-dark: #4a3833;
    --photo-mid: #c9b1a4;
    --photo-light: #f3efec;
    --desk-wood: #a9744a;
    --desk-light: #d8c3a8;
  }
  * { margin: 0; padding: 0; box-sizing: border-box; }
  html, body {
    width: 1200px; height: 1023px; overflow: hidden;
    background: var(--backdrop);
    font-family: "Lato", sans-serif;
  }
  .sheet { position: relative; width: 1200px; height: 1023px; }
  .card {
    position: absolute; left: 200px; width: 800px; height: 457px;
    border-radius: 22px; overflow: hidden;
    box-shadow: 0 10px 28px rgba(0,0,0,.18);
  }
  /* Front */
  .card-front {
    top: 36px;
    background: linear-gradient(180deg, var(--card-white) 0%, var(--card-shade) 100%);
  }
  .front-band {
    position: absolute; left: 0; right: 0; bottom: 0; height: 58px;
    background: linear-gradient(180deg, var(--yellow) 0%, var(--yellow-deep) 100%);
  }
  .portrait {
    position: absolute; left: 40px; top: 180px; width: 290px; height: 205px;
    border-radius: 6px;
    background: linear-gradient(135deg, var(--photo-dark) 0%, var(--photo-mid) 45%, var(--photo-light) 100%);
  }
  .divider {
    position: absolute; left: 300px; top: 164px; width: 340px; height: 1.5px;
    background: var(--gold-line);
  }
  .identity { position: absolute; left: 360px; top: 48px; }
  .name {
    font-size: 30px; line-height: 36px; font-weight: 700;
    color: var(--gold); letter-spacing: .2px;
  }
  .role, .region {
    font-size: 19px; line-height: 26px; color: var(--ink); margin-top: 2px;
  }
  .contacts {
    position: absolute; left: 360px; top: 184px; list-style: none;
  }
  .contacts li {
    display: flex; align-items: center; gap: 12px;
    font-size: 19px; line-height: 31px; color: var(--ink); height: 31px;
  }
  .icon { width: 18px; height: 18px; flex: none; }
  /* Back */
  .card-back { top: 530px; background: var(--desk-wood); }
  .back-band-top {
    position: absolute; left: 0; right: 0; top: 0; height: 92px;
    background: linear-gradient(180deg, var(--yellow) 0%, var(--yellow-deep) 100%);
  }
  .back-band-bottom {
    position: absolute; left: 0; right: 0; bottom: 0; height: 92px;
    background: linear-gradient(180deg, var(--orange) 0%, var(--orange-deep) 100%);
  }
  .workspace-photo {
    position: absolute; left: 0; right: 0; top: 92px; bottom: 92px;
    background: linear-gradient(120deg, var(--desk-wood) 0%, var(--desk-light) 45%, var(--desk-wood) 100%);
  }
</style>
</head>
<body>
<main class="sheet">
  <section class="card card-front" aria-label="Business card front">
    <div class="portrait" role="img" aria-label="Portrait photograph of Morven Quillet"></div>
    <div class="divider"></div>
    <header class="identity">
      <h1 class="name">Morven Quillet</h1>
      <p class="role">Communications &amp; Campaign strategist</p>
      <p class="region">Sydney - Melbourne</p>
    </header>
    <ul class="contacts">
      <li>
        <svg class="icon" viewBox="0 0 18 18"><rect x="1" y="1" width="16" height="16" rx="3" fill="none" stroke="var(--gold)" stroke-width="1.6"/><rect x="6" y="4" width="6" height="10" rx="1.2" fill="none" stroke="var(--gold)" stroke-width="1.3"/></svg>
        0498 317 250
      </li>
      <li>
        <svg class="icon" viewBox="0 0 18 18"><rect x="0" y="0" width="18" height="18" rx="3" fill="var(--gold)"/><rect x="3.5" y="5" width="11" height="8" fill="none" stroke="#fff" stroke-width="1.3"/><path d="M3.5 5 L9 9.5 L14.5 5" fill="none" stroke="#fff" stroke-width="1.3"/></svg>
        morven@morvenquillet.example
      </li>
      <li>
        <svg class="icon" viewBox="0 0 18 18"><rect x="1" y="1" width="16" height="16" rx="3" fill="none" stroke="var(--gold)" stroke-width="1.6"/></svg>
        morvenquillet
      </li>
      <li>
        <svg class="icon" viewBox="0 0 18 18"><rect x="0" y="0" width="18" height="18" rx="3" fill="var(--gold)"/><circle cx="9" cy="9" r="5" fill="none" stroke="#fff" stroke-width="1.3"/><path d="M4 9 H14 M9 4 C6.5 7 6.5 11 9 14 M9 4 C11.5 7 11.5 11 9 14" fill="none" stroke="#fff" stroke-width="1"/></svg>
        morvenquillet.example
      </li>
      <li>
        <svg class="icon" viewBox="0 0 18 18"><rect x="0" y="0" width="18" height="18" rx="3" fill="var(--gold)"/></svg>
        @morvenquillet
      </li>
    </ul>
    <div class="front-band"></div>
  </section>

  <section class="card card-back" aria-label="Business card back">
    <div class="back-band-top"></div>
    <div class="workspace-photo" role="img" aria-label="Overhead photograph of a team working around a wooden desk with laptops, papers and plants"></div>
    <div class="back-band-bottom"></div>
  </section>
</main>
</body>
</html>
```